Business Card Design

I need a Business Card that will catch the attention that will not get thrown in a Drawer. I have 23 companies I use for Auto, Home, Life, and Business Insurance. I make sure that people have the best coverage for the $ spent.

Industry/Entity Type

Business

Contact Information for Business Card

Dorlin Insurance Agency, Inc., Marcus Helgren, 4375 West Tamber Lane Tamberly, Norvale 45192 555-281-7496, www.dorlinagency.example, Friendlo, Netlinkr, Circlely

```html
<!DOCTYPE html>
<html lang="en">
<head>
<meta charset="utf-8">
<title>Dorlin Insurance Agency – Business Card</title>
<link rel="stylesheet" href="https://fonts.googleapis.com/css2?family=Bebas+Neue&family=Cinzel:wght@400&display=swap">
<style>
  :root {
    --band-top: #766253;
    --band-name: #4e4037;
    --field-base: #7a6453;
    --field-shade: #5e4c40;
    --ink: #ffffff;
  }
  html, body {
    margin: 0;
    padding: 0;
    overflow: hidden;
    background: #e9e5e1;
  }
  .card {
    position: relative;
    width: 1200px;
    height: 692px;
    overflow: hidden;
    background: var(--field-base);
    color: var(--ink);
    font-family: "Bebas Neue", "Arial Narrow", sans-serif;
  }
  .agency-band {
    position: absolute;
    left: 0; top: 0;
    width: 100%; height: 211px;
    background: var(--band-top);
  }
  .agency-name {
    position: absolute;
    left: 0; right: 0; top: 90px;
    margin: 0;
    text-align: center;
    font-family: "Cinzel", "Times New Roman", serif;
    font-weight: 400;
    font-size: 56px;
    letter-spacing: 1.5px;
    line-height: 1;
  }
  .name-band {
    position: absolute;
    left: 0; top: 211px;
    width: 100%; height: 156px;
    background: var(--band-name);
    box-shadow: 0 6px 10px rgba(0,0,0,0.35);
    z-index: 2;
  }
  .agent-name {
    position: absolute;
    left: 0; right: 0; top: 38px;
    margin: 0;
    text-align: center;
    font-weight: 400;
    font-size: 98px;
    letter-spacing: 6px;
    line-height: 1;
  }
  .texture-field {
    position: absolute;
    left: 0; top: 367px;
    width: 100%; height: 325px;
    background: linear-gradient(180deg, var(--field-shade) 0%, var(--field-base) 30%, var(--field-base) 100%);
  }
  .address {
    position: absolute;
    left: 0; right: 0; top: 404px;
    margin: 0;
    text-align: center;
    font-style: normal;
    font-size: 54px;
    letter-spacing: 2px;
    line-height: 68px;
    z-index: 3;
  }
  .contact-row {
    position: absolute;
    left: 0; top: 600px;
    width: 100%;
    height: 60px;
    z-index: 3;
    font-size: 46px;
    letter-spacing: 1.5px;
    line-height: 60px;
  }
  .phone { position: absolute; left: 47px; top: 0; }
  .website { position: absolute; left: 406px; top: 0; }
  .social-list {
    position: absolute;
    right: 30px; top: 4px;
    margin: 0; padding: 0;
    list-style: none;
    display: flex;
    gap: 18px;
    font-size: 22px;
    letter-spacing: 0.5px;
    line-height: 52px;
    white-space: nowrap;
  }
</style>
</head>
<body>
  <main class="card">
    <header class="agency-band">
      <h1 class="agency-name">Dorlin Insurance Agency, Inc.</h1>
    </header>

    <section class="name-band">
      <h2 class="agent-name">Marcus Helgren</h2>
    </section>

    <div class="texture-field" role="img" aria-label="Diagonal stripe texture in warm browns"></div>

    <address class="address">
      4375 West Tamber Lane<br>
      Tamberly, Norvale 45192
    </address>

    <footer class="contact-row">
      <span class="phone">555-281-7496</span>
      <span class="website">WWW.DORLINAGENCY.EXAMPLE</span>
      <ul class="social-list">
        <li>Friendlo</li>
        <li>Netlinkr</li>
        <li>Circlely</li>
      </ul>
    </footer>
  </main>
</body>
</html>
```